Dog care service needs business card design

Our company is Pawsome Haven. We provide care for dogs while their owners are away, either through home visits or a holiday stay in the homes of carefully selected minders. Our existing website & Chatterbook cover should provide all the colour cues for our business cards - namely blues, blondes and grey. We have an existing logo (provided).

www.pawsomehaven-demo.com.au
www.chatterbook-demo.com/pawsomehavenau

We wish to clearly communicate our three areas of service "dog minding, home visits, dog walking".

We would like to have the files ready for upload to Prontoprint (or similar) for immediate printing.

Target Market(s)

Dog owners who love their dogs like family

Industry/Entity Type

Business

Contact Information for Business Card

Pawsome Haven
Ph: 0491 574 318

Font styles to use
Sans Serif

Colors
33a6d7
3176b5

Requirements
Must have
• Logo
• Telephone number
• website
• "Dog minding, home visits, dog walking"
Should not have
• any additional illustrations beyond the logo.

```html
<!DOCTYPE html>
<html lang="en">
<head>
<meta charset="utf-8">
<title>Pawsome Haven – Business Card</title>
<link href="https://fonts.googleapis.com/css2?family=Montserrat:wght@600&family=Questrial&display=swap" rel="stylesheet">
<style>
  :root {
    --page-bg: #e4e3e1;
    --slate: #3b4350;
    --slate-dark: #323945;
    --ink: #454c57;
    --muted: #6b7079;
    --sky: #33a6d7;
    --ocean: #3176b5;
    --paper: #ffffff;
    --paper-shade: #eeeff0;
    --soft-white: #e9ecef;
  }
  * { margin: 0; padding: 0; box-sizing: border-box; }
  html, body { width: 1200px; height: 871px; overflow: hidden; }
  body {
    background: var(--page-bg);
    font-family: "Questrial", "Century Gothic", sans-serif;
    position: relative;
  }
  .card {
    position: absolute;
    top: 287px;
    width: 520px;
    height: 297px;
    border-radius: 4px;
    box-shadow: 0 10px 26px rgba(0,0,0,.22);
    overflow: hidden;
  }

  /* Back side */
  .card-back {
    left: 50px;
    background: linear-gradient(135deg, var(--slate) 0%, var(--slate-dark) 100%);
    color: var(--soft-white);
  }
  .card-back .brand-mark {
    position: absolute;
    left: 48px;
    top: 112px;
    display: flex;
    align-items: center;
    gap: 12px;
  }
  .brand-dot {
    width: 22px; height: 22px; border-radius: 50%;
    background: var(--sky);
    flex: none;
  }
  .card-back .brand-name {
    font-family: "Montserrat", sans-serif;
    font-weight: 600;
    font-size: 26px;
    color: var(--soft-white);
    line-height: 1.1;
  }
  .service-list {
    position: absolute;
    left: 300px;
    top: 92px;
    list-style: none;
  }
  .service-list li {
    display: flex;
    align-items: center;
    gap: 14px;
    font-size: 19px;
    letter-spacing: .5px;
    margin-bottom: 12px;
  }
  .service-list svg { width: 14px; height: 12px; flex: none; }

  /* Front side */
  .card-front {
    left: 630px;
    background: linear-gradient(160deg, var(--paper) 0%, var(--paper) 55%, var(--paper-shade) 100%);
    color: var(--ink);
  }
  .card-front .brand-mark {
    position: absolute;
    top: 52px;
    left: 0; right: 0;
    display: flex;
    justify-content: center;
    align-items: center;
    gap: 12px;
  }
  .card-front .brand-name {
    font-family: "Montserrat", sans-serif;
    font-weight: 600;
    font-size: 32px;
    color: var(--ink);
  }
  .business-name {
    position: absolute;
    top: 138px;
    width: 100%;
    text-align: center;
    font-family: "Montserrat", sans-serif;
    font-weight: 600;
    font-size: 19px;
    letter-spacing: 1px;
    color: var(--ink);
  }
  .contact-row {
    position: absolute;
    top: 184px;
    left: 34px;
    right: 28px;
    display: flex;
    justify-content: space-between;
    font-size: 14px;
    color: var(--muted);
  }
  .contact-item { display: flex; align-items: center; gap: 10px; }
  .contact-item svg { width: 17px; height: 17px; flex: none; }
  .social-band {
    position: absolute;
    left: 0; right: 0; bottom: 0;
    height: 60px;
    background: var(--slate);
    display: flex;
    align-items: center;
    padding-left: 34px;
    gap: 12px;
    color: var(--paper);
    font-size: 14px;
    font-weight: 400;
    letter-spacing: .3px;
  }
  .social-square {
    width: 20px; height: 20px;
    background: var(--ocean);
    border: 1.5px solid var(--paper);
    flex: none;
  }
</style>
</head>
<body>

<section class="card card-back" aria-label="Business card back">
  <div class="brand-mark">
    <span class="brand-dot"></span>
    <span class="brand-name">Pawsome<br>Haven</span>
  </div>
  <ul class="service-list">
    <li><svg viewBox="0 0 14 12"><polyline points="1.5,6.5 5.5,10 12.5,1.5" fill="none" stroke="#33a6d7" stroke-width="2.4" stroke-linecap="round" stroke-linejoin="round"/></svg>Dog minding</li>
    <li><svg viewBox="0 0 14 12"><polyline points="1.5,6.5 5.5,10 12.5,1.5" fill="none" stroke="#33a6d7" stroke-width="2.4" stroke-linecap="round" stroke-linejoin="round"/></svg>home visits</li>
    <li><svg viewBox="0 0 14 12"><polyline points="1.5,6.5 5.5,10 12.5,1.5" fill="none" stroke="#33a6d7" stroke-width="2.4" stroke-linecap="round" stroke-linejoin="round"/></svg>dog walking</li>
  </ul>
</section>

<section class="card card-front" aria-label="Business card front">
  <div class="brand-mark">
    <span class="brand-dot"></span>
    <span class="brand-name">Pawsome Haven</span>
  </div>
  <p class="business-name">Pawsome Haven</p>
  <div class="contact-row">
    <span class="contact-item">
      <svg viewBox="0 0 24 24" aria-hidden="true"><path d="M6.6 10.8a15.1 15.1 0 0 0 6.6 6.6l2.2-2.2a1 1 0 0 1 1-.25 11.4 11.4 0 0 0 3.6.57 1 1 0 0 1 1 1V20a1 1 0 0 1-1 1A17 17 0 0 1 3 4a1 1 0 0 1 1-1h3.5a1 1 0 0 1 1 1c0 1.25.2 2.45.57 3.6a1 1 0 0 1-.25 1z" fill="#33a6d7"/></svg>
      0491 574 318
    </span>
    <span class="contact-item">
      <svg viewBox="0 0 24 24" aria-hidden="true" fill="none" stroke="#33a6d7" stroke-width="1.8"><circle cx="12" cy="12" r="9.5"/><ellipse cx="12" cy="12" rx="4" ry="9.5"/><line x1="2.5" y1="12" x2="21.5" y2="12"/><line x1="4" y1="7" x2="20" y2="7"/><line x1="4" y1="17" x2="20" y2="17"/></svg>
      www.pawsomehaven-demo.com.au
    </span>
  </div>
  <div class="social-band">
    <span class="social-square"></span>
    <span>www.chatterbook-demo.com/pawsomehavenau</span>
  </div>
</section>

</body>
</html>
```